Vocational Mentor needs an impressive business card

1. I need a business card (or maybe three with identic look) to promote me and my three business titles/services:
- Vocational Mentor. I help people find their vocation and live happily from it. I use my 20 years of experience in business, management and psychology to help them identify the most efficient ways to make a living doing what they are passionate about.
- Business Angel. I help founders start a succesful business with minimum risks and costs. I use my 20 years of experience in sales, management and entrepreneurship to help them identify the most efficient ways, in terms of time and cost, to validate their business idea.
- Learning Designer. I design unique learning programs that produce long-term cognitive and behavioural changes to people and organisations. I use my 20 years of experience in learning, teaching and change management to create minimalist experiences and processes that allow them to change efficiently in their pursued direction.

2. I would like a two-sided business card, on the front with my name, contact details and titles, on the back the explanation of the services.
Updates

Hi all,

I updated my brief, included contacts info and give feedback on all designs I got. I am new on this platform so please tell me if you need anything else or if I don't use corectly the platform forms.

Kind regards,
Mirel

Hi all,

I shortened the services description by deleting the phrase "I call..."

Kind regards,
Mirel

Target Market(s)

Freelancers, startups, people and organization willing to invest in change through ultimate learning experiences

Industry/Entity Type

Business

Font styles to use
Serif

Requirements
Must have
• Front side: full name, titles, web site, email, phone like below:
Mirel Vantaru
Vocational Mentor, Business Angel, Learning Designer
info@mirelvantaru.example
www.mirelvantaru.example
+40-748-MIRELV
Nice to have
• Back side: the description of the services I provide as in the task description.
1/3: it would be nice if I can jam all three titles on the front side but then I need a solution to jam all three services on the back side.

```html
<!DOCTYPE html>
<html lang="en">
<head>
<meta charset="utf-8">
<title>Mirel Vantaru – Business Card</title>
<link rel="stylesheet" href="https://fonts.googleapis.com/css2?family=Source+Sans+3:wght@300;400;700&display=swap">
<style>
  :root {
    --backdrop: #1b1d20;
    --front-card: #131313;
    --back-card: #2c2825;
    --name: #3a4a4c;
    --name-edge: #8aa6a8;
    --title: #7a8d90;
    --contact: #7a8b8e;
    --heading: #74d4ee;
    --body: #a89c90;
    --body-shadow: rgba(0,0,0,0.65);
    --smoke-a: rgba(150,190,190,0.28);
    --smoke-b: rgba(150,190,190,0);
  }
  * { box-sizing: border-box; margin: 0; padding: 0; }
  html, body {
    width: 1200px; height: 675px; overflow: hidden;
    background: var(--backdrop);
    font-family: "Source Sans 3", "Myriad Pro", sans-serif;
  }
  .canvas {
    position: relative; width: 1200px; height: 675px;
    display: flex; align-items: center; justify-content: center; gap: 40px;
  }
  .card {
    position: relative; width: 540px; height: 310px; overflow: hidden;
    box-shadow: 0 10px 30px rgba(0,0,0,0.55);
  }
  .card--front { background: var(--front-card); }
  .card--back { background: var(--back-card); }

  .smoke {
    position: absolute; pointer-events: none;
    background: radial-gradient(ellipse at center, var(--smoke-a) 0%, var(--smoke-b) 70%);
  }
  .card--front .smoke {
    left: 90px; top: 60px; width: 360px; height: 220px;
    transform: rotate(-28deg);
  }
  .card--back .smoke {
    left: -40px; top: 0; width: 140px; height: 280px;
    transform: rotate(12deg); opacity: 0.6;
  }

  .identity {
    position: absolute; left: 250px; top: 78px; text-align: center; width: 220px;
  }
  .identity__name {
    font-weight: 700; font-size: 21px; letter-spacing: 0.5px;
    color: var(--name);
    text-shadow: 1px 1px 0 #000, 0 0 3px rgba(0,0,0,0.9);
    -webkit-text-stroke: 0.6px var(--name-edge);
  }
  .identity__titles {
    list-style: none; margin-top: 4px;
    font-weight: 300; font-size: 18px; line-height: 21px; color: var(--title);
  }
  .contacts {
    position: absolute; left: 268px; top: 208px; list-style: none;
    font-size: 13px; line-height: 16px; color: var(--contact);
  }
  .contacts li { display: flex; align-items: center; gap: 6px; }
  .contacts svg { width: 11px; height: 11px; flex: none; }

  .services { position: absolute; left: 58px; top: 34px; right: 30px; }
  .service { margin-bottom: 10px; }
  .service__title {
    font-weight: 700; font-size: 13px; color: var(--heading); margin-bottom: 3px;
  }
  .service__text {
    font-size: 11px; line-height: 13px; color: var(--body);
    text-shadow: 0 1px 1px var(--body-shadow);
  }
</style>
</head>
<body>
<main class="canvas">
  <section class="card card--front" aria-label="Front side">
    <div class="smoke" role="img" aria-label="Soft teal smoke swirl decoration"></div>
    <div class="identity">
      <h1 class="identity__name">Mirel Vantaru</h1>
      <ul class="identity__titles">
        <li>Vocational Mentor</li>
        <li>Business Angel</li>
        <li>Learning Designer</li>
      </ul>
    </div>
    <ul class="contacts">
      <li>
        <svg viewBox="0 0 12 12" fill="none" stroke="currentColor" stroke-width="1"><rect x="1" y="2.5" width="10" height="7"/><path d="M1 2.5l5 4 5-4"/></svg>
        info@mirelvantaru.example
      </li>
      <li>
        <svg viewBox="0 0 12 12" fill="none" stroke="currentColor" stroke-width="1"><circle cx="6" cy="6" r="5"/><path d="M1 6h10M6 1c-2.5 3-2.5 7 0 10M6 1c2.5 3 2.5 7 0 10"/></svg>
        www.mirelvantaru.example
      </li>
      <li>
        <svg viewBox="0 0 12 12" fill="none" stroke="currentColor" stroke-width="1"><rect x="1" y="3" width="10" height="7" rx="1"/><path d="M3 3V1.5h6V3M4 6.5h4"/></svg>
        +40-748-MIRELV
      </li>
    </ul>
  </section>

  <section class="card card--back" aria-label="Back side">
    <div class="smoke" role="img" aria-label="Faint teal smoke swirl decoration"></div>
    <div class="services">
      <article class="service">
        <h2 class="service__title">Vocational Mentor</h2>
        <p class="service__text">I help people to find their vocation and live happily from it. I use my 20 years of experience in business, management and psychology to help them identify the most efficient ways to make a living doing what they are passionate about. I call this service vocational mentoring.</p>
      </article>
      <article class="service">
        <h2 class="service__title">Business Angel</h2>
        <p class="service__text">I help founders to start a succesful business with minimum risks and costs. I use my 20 years of experience in sales, management and entrepreneurship to help them identify the most efficient ways, in terms of time and cost, to validate their business idea. I call this service lean-startup mentoring.</p>
      </article>
      <article class="service">
        <h2 class="service__title">Learning Designer</h2>
        <p class="service__text">I design unique learning programs that produce long-term cognitive and behavioural changes to people and organisations. I use my 20 years of experience in learning, teaching and change management to create minimalist experiences and processes that allows them to change efficiently in their pursued direction. I call this service ultimate learning design.</p>
      </article>
    </div>
  </section>
</main>
</body>
</html>
```